Carpentry company Needs a business card design

We need a design for a Carpentry / building company, business card. Please think of designs out of the ordinary and try to make it eye catching. Our existing logo will need to be incorporated in the design. However feel free to change the colours of the logo to suit your design. I would like to see some designs with green /black and orange incorporated into it.These are not the only colours accepted and all designs that appeal will be accepted.

Please contact me should you have any questions
Thanks Martin

Target Market(s)

General Public seeking carpentry work

Industry/Entity Type

Business

Contact Information for Business Card

- Current company logo ( colours can be changed)
-Phone number ,
- info@brelvanbuild.com.au
- brelvanbuild.com.au
-the facebook symbol

Font styles to use
Other font styles liked:
• You choose

Requirements
Must have
• Services we provide
• - Renovations
• -Deckings & Pergolas
• -Kitchens
• - Bathrooms
• - Intricate details
Nice to have
• an awesome design
Should not have
• Tools on the business card

```html
<!DOCTYPE html>
<html lang="en">
<head>
<meta charset="utf-8">
<title>Brelvan Build – Business Card</title>
<link rel="stylesheet" href="https://fonts.googleapis.com/css2?family=Open+Sans:wght@400;600;700;800&display=swap">
<style>
  :root {
    --brown: #3a2628;
    --gold: #d8a45a;
    --orange: #d4892b;
    --paper: #ffffff;
    --backdrop: #3c3c3e;
    --ink: #2a1c1d;
  }
  * { margin: 0; padding: 0; box-sizing: border-box; }
  html, body { width: 1200px; height: 1200px; overflow: hidden; }
  body {
    background: var(--backdrop);
    font-family: "Open Sans", Arial, sans-serif;
    position: relative;
  }
  .card {
    position: absolute;
    left: 220px;
    width: 760px;
    height: 434px;
    overflow: hidden;
  }
  .card--front { top: 110px; background: var(--brown); }
  .card--back { top: 630px; background: var(--paper); }

  .wordmark {
    position: absolute;
    display: flex;
    align-items: center;
    gap: 14px;
    font-weight: 800;
    letter-spacing: 2px;
    white-space: nowrap;
  }
  .wordmark__square { display: block; background: var(--gold); }
  .card--front .wordmark {
    left: 50%; top: 50%;
    transform: translate(-50%, -50%);
    font-size: 58px;
    color: var(--paper);
  }
  .card--front .wordmark__square { width: 26px; height: 26px; }
  .card--back .wordmark {
    left: 48px; top: 70px;
    font-size: 44px;
    color: var(--brown);
  }
  .card--back .wordmark__square { width: 20px; height: 20px; }

  .card__band { position: absolute; inset: 0; }

  .person {
    position: absolute;
    right: 48px; top: 118px;
    text-align: right;
  }
  .person__name {
    font-size: 27px; font-weight: 700; letter-spacing: 1.5px;
    color: var(--orange);
  }
  .person__role {
    font-size: 15px; font-weight: 800; color: var(--ink); margin-top: 6px;
  }

  .services {
    position: absolute;
    left: 40px; right: 40px; top: 224px;
    display: flex; justify-content: space-between;
    font-size: 15px; color: var(--ink);
  }
  .services__sep { color: var(--orange); font-size: 10px; align-self: center; }

  .contact {
    position: absolute;
    list-style: none;
    color: var(--paper);
    font-size: 17px;
  }
  .contact li { display: flex; align-items: center; gap: 12px; margin-bottom: 10px; }
  .contact--left { left: 36px; top: 300px; }
  .contact--right { left: 430px; top: 340px; }
  .contact__icon {
    width: 20px; height: 20px; border-radius: 3px;
    background: var(--gold); flex: none;
    display: flex; align-items: center; justify-content: center;
  }
</style>
</head>
<body>

  <section class="card card--front" aria-label="Card front">
    <div class="wordmark">
      <span class="wordmark__square"></span>
      <span class="wordmark__name">BRELVAN BUILD</span>
    </div>
  </section>

  <section class="card card--back" aria-label="Card back">
    <svg class="card__band" viewBox="0 0 760 434" preserveAspectRatio="none" aria-hidden="true">
      <polyline points="0,206 26,206 42,192 58,206 640,206 700,206 716,192 732,206 760,206"
                fill="none" stroke="var(--brown)" stroke-width="3"/>
      <polygon points="0,262 40,262 56,276 72,262 700,262 716,250 732,262 760,262 760,434 0,434"
               fill="var(--brown)"/>
    </svg>

    <div class="wordmark">
      <span class="wordmark__square"></span>
      <span class="wordmark__name">BRELVAN BUILD</span>
    </div>

    <div class="person">
      <p class="person__name">DAVID MARTIN</p>
      <p class="person__role">DIRECTOR</p>
    </div>

    <p class="services">
      <span>Renovations</span><span class="services__sep">◆</span>
      <span>Deckings &amp; Pergolas</span><span class="services__sep">◆</span>
      <span>Kitchens</span><span class="services__sep">◆</span>
      <span>Bathrooms</span><span class="services__sep">◆</span>
      <span>Intricate details</span>
    </p>

    <ul class="contact contact--left">
      <li>
        <span class="contact__icon">
          <svg width="13" height="13" viewBox="0 0 24 24"><path fill="var(--brown)" d="M6.6 10.8a15.1 15.1 0 0 0 6.6 6.6l2.2-2.2c.3-.3.7-.4 1-.2 1.1.4 2.3.6 3.6.6.6 0 1 .4 1 1V20c0 .6-.4 1-1 1A17 17 0 0 1 3 4c0-.6.4-1 1-1h3.5c.6 0 1 .4 1 1 0 1.3.2 2.5.6 3.6.1.3 0 .7-.2 1z"/></svg>
        </span>
        <span>0400 555 218</span>
      </li>
      <li>
        <span class="contact__icon">
          <svg width="13" height="11" viewBox="0 0 24 18"><rect x="1" y="1" width="22" height="16" fill="none" stroke="var(--brown)" stroke-width="2"/><polyline points="1,1 12,10 23,1" fill="none" stroke="var(--brown)" stroke-width="2"/></svg>
        </span>
        <span>info@brelvanbuild.com.au</span>
      </li>
    </ul>

    <ul class="contact contact--right">
      <li><span class="contact__icon"></span><span>brelvanbuild</span></li>
      <li><span class="contact__icon"></span><span>brelvanbuild.com.au</span></li>
    </ul>
  </section>

</body>
</html>
```